Publisher needs a book cover design for ‘Lanterns Over the Marsh Gate’ book

We need a book cover (front, back, spine) for the 2nd edition of a book entitled ‘Lanterns Over the Marsh Gate’ and subtitled ‘the quiet geography of tidal winds, ferry routes and harbour lanterns’ (inverted commas not to be part of the title and subtitle). The author is Rupert Calloway. The publisher is Vellmark Press. The finished size of the paperback version will be the industry standard 9" x 6". There will be paperback, hardback, and e-book versions. The final number of pages is expected to be in the region 150-180 pages. Text for the back cover is not yet available, but at the bottom of the back cover should be publisher logo (rectangular) on the left and space for the ISBN bar code on the right. The circular logo should be on the spine. The design should be original and not include any stock images that have been created by someone else or may require obtaining a copyright licence to use. Symbols in common use and not copyrighted are probably ok. There are no required images, photographs or symbols except the publisher logo at the left bottom of the back cover and lower spine. Spine lettering should be UK/US style with the top of the writing nearest the front cover. The designer is free to be creative using appropriate diagrams, symbols or abstract designs. Rectangular and circular variants of the publisher logo are attached. Designers are assured that when evaluating designs absolutely no notice whatsoever is taken of a designer's Pixo Rally ranking or status; We are completely output driven, so what matters is the design, not the ranking or status of the designer. In a similar way, designs are not evaluated as 'good' or 'bad' - the winning design will be chosen after review by a design review panel and is not decided arbitrarily by a single person. All submitted designs should be capable of effective copyright assignment.

Target Market(s)

Practitioners, parents, teachers, pupils and academics concerned with child protection, safeguarding and the elimination of emotional abuse of children in the classroom

Font styles to use
Serif
Sans Serif

Requirements
Must have
• • Title, author, edition, subtitle, publisher logo
Nice to have
• • Originality, innovation
Should not have
• • Stock images or anything else requiring additional copyright discussions and negotiations.

```html
<!DOCTYPE html>
<html lang="en">
<head>
<meta charset="utf-8">
<title>Lanterns Over the Marsh Gate — Cover</title>
<link rel="stylesheet" href="https://fonts.googleapis.com/css2?family=Bebas+Neue&family=League+Gothic&family=Pathway+Gothic+One&family=Crimson+Pro:wght@400;500&family=Raleway:wght@400;700&family=Roboto+Condensed:wght@400;700&display=swap">
<style>
  :root {
    --back-bg: #e6e7e8;
    --front-light: #fbfbfb;
    --front-mid: #e4e5e6;
    --splash: #d2d3d5;
    --ink: #231f20;
    --title-grey: #808285;
    --badge-red: #ed1c24;
    --white: #ffffff;
    --box-bg: #f3f3f4;
  }
  * { margin: 0; padding: 0; box-sizing: border-box; }
  html, body { width: 1200px; height: 872px; overflow: hidden; background: var(--white); }
  .cover { position: relative; width: 1200px; height: 872px; overflow: hidden; background: var(--back-bg); }

  /* Back cover */
  .back-blurb {
    position: absolute; left: 75px; top: 70px; width: 448px;
    font-family: "Pathway Gothic One", sans-serif; font-size: 29px; line-height: 36.3px;
    color: var(--ink);
  }
  .author-box {
    position: absolute; left: 75px; top: 539px; width: 438px; height: 137px;
    background: var(--box-bg);
  }
  .author-photo {
    position: absolute; left: 17px; top: 11px; width: 94px; height: 114px; background: var(--white);
  }
  .author-bio {
    position: absolute; left: 122px; top: 10px; width: 312px;
    font-family: "Crimson Pro", serif; font-size: 13.6px; line-height: 15.7px; color: var(--ink);
  }
  .author-bio h3 { font-weight: 500; font-size: 14.5px; }
  .publisher-mark {
    position: absolute; left: 77px; top: 716px; display: flex; align-items: center; gap: 8px;
    font-family: "Crimson Pro", serif; font-size: 25px; color: var(--ink); letter-spacing: 1px;
  }
  .publisher-mark .dot { width: 44px; height: 44px; border-radius: 50%; background: var(--ink); }
  .isbn-space { position: absolute; left: 384px; top: 696px; width: 129px; height: 85px; background: var(--white); }

  /* Spine */
  .spine { position: absolute; left: 572px; top: 0; width: 51px; height: 872px; }
  .spine-text {
    position: absolute; writing-mode: vertical-rl; color: var(--ink); white-space: nowrap;
  }
  .spine-title { left: 24px; top: 78px; font-family: "Roboto Condensed", sans-serif; font-weight: 700; font-size: 21px; letter-spacing: 0.5px; }
  .spine-subtitle { left: 9px; top: 78px; font-family: "Raleway", sans-serif; font-size: 9.6px; }
  .spine-edition { left: 16px; top: 524px; font-family: "Raleway", sans-serif; font-size: 15px; }
  .spine-author { left: 12px; top: 640px; font-family: "Raleway", sans-serif; font-weight: 700; font-size: 15.5px; line-height: 14px; }
  .spine-publisher { left: 18px; top: 770px; display: flex; align-items: center; gap: 4px;
    font-family: "Raleway", sans-serif; font-size: 8px; letter-spacing: 1px; }
  .spine-publisher .dot { width: 14px; height: 14px; border-radius: 50%; background: var(--ink); }

  /* Front cover */
  .front { position: absolute; left: 623px; top: 0; width: 577px; height: 872px; }
  .front svg { display: block; }
</style>
</head>
<body>
<div class="cover">

  <section class="back">
    <p class="back-blurb">Lorem ipsum dolor sit amet, consectetur adipiscing elit, sed do eiusmod tempor incididunt ut labore et dolore magna aliqua. Ut enim ad minim veniam, quis nostrud exercitation ullamco laboris nisi ut aliquip ex ea commodo consequat. Duis aute irure dolor in reprehenderit in voluptate velit esse cillum dolore eu fugiat nulla pariatur. Excepteur sint occaecat cupidatat non proident, sunt in culpa qui officia deserunt mollit anim id est laborum.</p>

    <div class="author-box">
      <div class="author-photo"></div>
      <div class="author-bio">
        <h3>Author</h3>
        <p>Lorem ipsum dolor sit amet, consectetur adipiscing elit, sed do eiusmod tempor incididunt ut labore et dolore magna aliqua. Ut enim ad minim veniam, quis nostrud exercitation ullamco laboris nisi ut aliquip ex ea commodo consequat. Duis aute irure dolor in reprehenderit in voluptate</p>
      </div>
    </div>

    <div class="publisher-mark"><span class="dot"></span><span>VELLMARK PRESS</span></div>
    <div class="isbn-space"></div>
  </section>

  <section class="spine">
    <span class="spine-text spine-title">LANTERNS OVER THE MARSH GATE</span>
    <span class="spine-text spine-subtitle">The Quiet Geography of Tidal Winds, Ferry Routes and Harbour Lanterns</span>
    <span class="spine-text spine-edition">2nd edition</span>
    <span class="spine-text spine-author">RUPERT<br>CALLOWAY</span>
    <span class="spine-text spine-publisher"><span class="dot"></span>VELLMARK</span>
  </section>

  <section class="front">
    <svg width="577" height="872" viewBox="0 0 577 872" xmlns="http://www.w3.org/2000/svg">
      <defs>
        <radialGradient id="front-wash" cx="0.6" cy="0.42" r="0.75">
          <stop offset="0" stop-color="var(--front-light)"/>
          <stop offset="0.55" stop-color="var(--front-mid)"/>
          <stop offset="1" stop-color="var(--splash)"/>
        </radialGradient>
        <linearGradient id="title-heat" x1="0" y1="0" x2="1" y2="0.2">
          <stop offset="0" stop-color="#9e1b32"/>
          <stop offset="0.3" stop-color="#e8213b"/>
          <stop offset="0.65" stop-color="#f7941d"/>
          <stop offset="1" stop-color="#fde21a"/>
        </linearGradient>
      </defs>

      <rect class="front-bg" width="577" height="872" fill="url(#front-wash)" role="img" aria-label="Soft grey abstract ink-splash texture"/>

      <g class="edition-badge">
        <circle cx="457" cy="113" r="69" fill="var(--white)"/>
        <text x="457" y="125" text-anchor="middle" font-family="Bebas Neue, sans-serif" font-size="78" fill="var(--badge-red)" transform="rotate(-6 457 113)">2nd</text>
        <text x="452" y="162" text-anchor="middle" font-family="Bebas Neue, sans-serif" font-size="38" fill="var(--badge-red)" transform="rotate(-6 457 113)">edition</text>
      </g>

      <g class="title">
        <text x="50" y="261" textLength="464" lengthAdjust="spacingAndGlyphs" font-family="Bebas Neue, sans-serif" font-size="120" fill="var(--title-grey)">LANTERNS</text>
        <text x="50" y="432" textLength="464" lengthAdjust="spacingAndGlyphs" font-family="Bebas Neue, sans-serif" font-size="224" fill="url(#title-heat)">OVER THE</text>
        <rect x="51" y="445" width="463" height="72" fill="var(--title-grey)"/>
        <text x="282" y="506" text-anchor="middle" textLength="434" lengthAdjust="spacingAndGlyphs" font-family="Bebas Neue, sans-serif" font-size="78" fill="var(--white)">MARSH GATE</text>
      </g>

      <g class="subtitle" font-family="Raleway, sans-serif" font-weight="700" font-size="26" fill="var(--ink)" text-anchor="middle">
        <text x="281" y="579">THE QUIET GEOGRAPHY OF</text>
        <text x="281" y="607.5">TIDAL WINDS, FERRY</text>
        <text x="281" y="636">ROUTES AND HARBOUR</text>
        <text x="281" y="664.5">LANTERNS</text>
      </g>

      <text class="author" x="102" y="826" textLength="362" lengthAdjust="spacingAndGlyphs" font-family="League Gothic, sans-serif" font-size="74" fill="var(--ink)" letter-spacing="3">RUPERT CALLOWAY</text>
    </svg>
  </section>

</div>
</body>
</html>
```